Bring my website out of the dark ages!

Website redesign for Velmar Consulting
www.velmarqx.com and www.trundlebox.ca
Currently dark (black), small font, boring, old
Want something simple, bright, fun, modern, clean and professional
Flexible content, any ideas appreciated
In business since 1998, focused on long term client relationships and being there when it matters.
Specialize solutions for clients based on their needs, vision and budget, not what the IT market thinks is the latest and greatest (and most profitable).
Want to eventually add helpful content (videos) and testimonials to the site for the benefit of the visitor

Target Market(s)

Anyone looking for IT services - target is a business with 25-100 employees.

Industry/Entity Type

It Company

Coding

Coded - Design and coding required

Number of Pages Required

4 page

Colors

Designer to choose colors to be used in the design.

Requirements
Must have
• Bright, clean, simple, no scrolling, fast
Nice to have
• Neat animation of some kind
Should not have
• scrolling
• too much information

```html
<!DOCTYPE html>
<html lang="en">
<head>
<meta charset="utf-8">
<title>Velmar Consulting</title>
<link rel="stylesheet" href="https://fonts.googleapis.com/css2?family=Open+Sans:wght@400;600;700&family=Source+Code+Pro:wght@400&display=swap">
<style>
  :root {
    --bg: #eeeeee;
    --white: #ffffff;
    --accent-blue: #86cdf5;
    --tag-pink: #e8308a;
    --ink: #333333;
    --rule: #d0d0d0;
    --badge: #cfcfcf;
    --photo-light: #dfe3e7;
    --photo-mid: #c9d6e2;
  }
  * { margin: 0; padding: 0; box-sizing: border-box; }
  html, body {
    width: 1200px; height: 609px; overflow: hidden;
    background: var(--bg);
    font-family: "Open Sans", sans-serif;
    color: var(--ink);
  }
  .page { position: relative; width: 1200px; height: 609px; }
  .trust-badge {
    position: absolute; left: 21px; top: 24px;
    width: 89px; height: 40px;
    display: flex; align-items: center; gap: 6px;
  }
  .trust-badge .seal { width: 38px; height: 38px; border-radius: 50%; background: var(--badge); }
  .trust-badge .plate { width: 46px; height: 26px; border-radius: 3px; background: var(--badge); }
  .hero-photo {
    position: absolute; left: 800px; top: 0;
    width: 400px; height: 574px;
    background: linear-gradient(160deg, var(--photo-light) 0%, var(--photo-mid) 55%, #e6e2dc 100%);
  }
  .hero {
    position: absolute; left: 112px; top: 220px; width: 576px;
  }
  .hero-title {
    font-size: 26px; font-weight: 700; color: var(--accent-blue);
    letter-spacing: 0.2px; line-height: 1.2;
    padding-bottom: 8px; border-bottom: 1px solid var(--rule);
  }
  .hero-title .tagline {
    font-size: 9px; font-weight: 400; color: var(--ink);
    letter-spacing: 0; margin-left: 4px;
  }
  .hero-body { margin: 13px 0 0 60px; width: 450px; }
  .tags {
    font-family: "Source Code Pro", monospace;
    font-size: 9px; color: var(--tag-pink); line-height: 14px;
  }
  .intro { font-size: 10.3px; line-height: 15.2px; margin-top: 1px; }
  .cta {
    display: inline-block; margin-top: 30px;
    background: var(--white); color: var(--ink);
    font-size: 10.5px; padding: 5px 8px; border-radius: 2px;
    text-decoration: none;
  }
  .site-bar {
    position: absolute; left: 0; top: 574px;
    width: 1200px; height: 35px; background: var(--white);
    display: flex; align-items: center; justify-content: space-between;
    padding: 0 258px 0 253px;
  }
  .brand { font-size: 13px; color: var(--ink); text-decoration: none; }
  .nav { display: flex; gap: 10px; list-style: none; }
  .nav a { font-size: 10px; color: var(--ink); text-decoration: none; }
</style>
</head>
<body>
<div class="page">
  <div class="trust-badge" aria-label="Security certificate badge">
    <span class="seal"></span><span class="plate"></span>
  </div>

  <div class="hero-photo" role="img" aria-label="Photo of a hand connecting white network cables in a server rack"></div>

  <section class="hero">
    <h1 class="hero-title">VELMAR CONSULTING INC <span class="tagline">server management specialists</span></h1>
    <div class="hero-body">
      <p class="tags">#installation #configuration #maintainance #support #security</p>
      <p class="intro">Our consultants offer businesses in Calgary; a monthly Service Maintenance Agreement to provide preventative measures for servers in any environment. These are essential in providing a stable and secure system for your business.</p>
      <a class="cta" href="#about">Find Out More</a>
    </div>
  </section>

  <footer class="site-bar">
    <a class="brand" href="#">Velmar Consulting</a>
    <ul class="nav">
      <li><a href="#about">About</a></li>
      <li><a href="#services">Services</a></li>
      <li><a href="#resources">Resources</a></li>
      <li><a href="#contact">Contact</a></li>
    </ul>
  </footer>
</div>
</body>
</html>
```